Multi product banner ads

We need a set of creatives containing various products within the same banner ad. For instance, a piece containing a cable offer, an insurance offer and a flight offer, no matter the size: MPU, skyscraper or Leaderboard.
The creative must contain multiple click tags, be compatible with Flash 10 and AS2. We would like to see proposals that replicate text ads and proposals that contain images and that are animated. Once we pick a format, we would need further help replicating to other industries.

Requirements
Must have
• at least 3 spaces for products on any given slide.
• compatible with Flash 10 and AS2
• <50KB

```html
<!DOCTYPE html>
<html lang="en">
<head>
<meta charset="utf-8">
<title>Multi Product Leaderboard</title>
<link href="https://fonts.googleapis.com/css2?family=Montserrat:wght@400;700&display=swap" rel="stylesheet">
<style>
  :root {
    --stage: #2f2d2e;
    --white: #ffffff;
    --band-blue: #4d7fd6;
    --ink: #4a4f5b;
    --offer-ink: #3b3b3b;
    --cta-red: #f1482c;
    --cta-ink: #ffffff;
  }
  html, body {
    margin: 0;
    padding: 0;
    width: 1200px;
    height: 900px;
    overflow: hidden;
    background: var(--stage);
    font-family: "Montserrat", Arial, sans-serif;
  }
  .canvas {
    position: relative;
    width: 1200px;
    height: 900px;
  }
  .leaderboard {
    position: absolute;
    left: 54px;
    top: 382px;
    width: 1092px;
    height: 136px;
    display: flex;
  }
  .brand-panel {
    width: 194px;
    height: 100%;
    background: var(--white);
    display: flex;
    align-items: center;
    justify-content: center;
  }
  .brand-name {
    font-weight: 700;
    font-size: 50px;
    letter-spacing: 1px;
    color: var(--ink);
    margin: 0;
  }
  .offer-band {
    flex: 1;
    height: 100%;
    background: var(--band-blue);
    position: relative;
  }
  .offer-card {
    position: absolute;
    top: 8px;
    width: 290px;
    height: 121px;
    display: flex;
    background: var(--white);
  }
  .offer-card--one { left: 10px; }
  .offer-card--two { left: 309px; }
  .offer-card--three { left: 607px; width: 291px; }
  .offer-visual {
    width: 150px;
    height: 100%;
    flex: none;
  }
  .offer-visual--business {
    background: linear-gradient(135deg, #d9c9b4 0%, #b9a58e 45%, #3f4a55 100%);
  }
  .offer-visual--flight {
    background: linear-gradient(160deg, #f4f6f8 0%, #dfe7ee 55%, #9fc3e4 100%);
  }
  .offer-visual--travel {
    background: linear-gradient(180deg, #bcd9f4 0%, #8fbfea 60%, #e9eef3 100%);
  }
  .offer-copy {
    flex: 1;
    display: flex;
    flex-direction: column;
  }
  .offer-text {
    flex: 1;
    margin: 0;
    padding: 16px 0 0 16px;
    font-size: 20px;
    line-height: 26px;
    font-weight: 400;
    color: var(--offer-ink);
  }
  .offer-cta {
    height: 40px;
    background: var(--cta-red);
    color: var(--cta-ink);
    font-weight: 700;
    font-size: 18px;
    display: flex;
    align-items: center;
    padding-left: 16px;
    text-decoration: none;
  }
</style>
</head>
<body>
<div class="canvas">
  <div class="leaderboard">
    <div class="brand-panel">
      <p class="brand-name">LOGO</p>
    </div>
    <div class="offer-band">
      <div class="offer-card offer-card--one">
        <div class="offer-visual offer-visual--business" role="img" aria-label="Photo of a businesswoman holding a passport and tickets"></div>
        <div class="offer-copy">
          <p class="offer-text">This is any<br>offer text</p>
          <a class="offer-cta" href="#">Learn more</a>
        </div>
      </div>
      <div class="offer-card offer-card--two">
        <div class="offer-visual offer-visual--flight" role="img" aria-label="Photo of a white passenger airplane model"></div>
        <div class="offer-copy">
          <p class="offer-text">This is any<br>offer text</p>
          <a class="offer-cta" href="#">Learn more</a>
        </div>
      </div>
      <div class="offer-card offer-card--three">
        <div class="offer-visual offer-visual--travel" role="img" aria-label="Photo of a smiling businessman flying against a blue sky"></div>
        <div class="offer-copy">
          <p class="offer-text">This is any<br>offer text</p>
          <a class="offer-cta" href="#">Learn more</a>
        </div>
      </div>
    </div>
  </div>
</div>
</body>
</html>
```